We need to design a new tradeshow booth for our company. We are Veltrane Engraving Systems and are the Authorized Distributor of laser products for QR Dyne. We are basically the USA branch of their group, representing their products. We stock, sell and distribute laser systems for this company. QRDyne is located in China. We also sell pad printing equipment and supplies, although this business is slowly becoming smaller as we focus more on lasers.

The parameters for the booth are as follows:

1) Our company logo should be on the tradeshow booth, as well as the QR Dyne logo. The QRDyne logo is provided and so will ours.
2) We would like to keep the tradeshow booth clean looking so the message comes across what we do very clear.
3) Pad printing should be emphasized on only one of the stands (attaches as file D), while the other stand (attached as file D) should emphasize laser products.
4) Laser Marking, Welding, Cleaning and Cutting are the four segments in which we operate. These make up the core of what lasers can do in a manufacturing environment. Most companies offer only specialize in one area but we can offer all four with the ability to supply 12 kilowatts of laser power, which is enough to cut through 40 mm of stainless steel.
5) Laser sources are many and operate in different wavelengths. Most companies only offer one source. We use four: Fiber, UV, CO2, and Green.
6) Continuous wave and Pulsed Options with Pico and Femto Lasers Available
7) Process Stationary and Moving Parts - Perfect for marking in packaging operations or on extrusion machinery.
8) Mark Graphics, Words, Bar codes, QR Codes and more. Maybe this gets incorporated next to marking section?
9) We custom build this machinery so we tailor it to the customer’s requirements with robotic integration possible.
10) Lasers Process Circuit Boards - Cut, Mark and Bore Holes that leave products much higher quality than traditional routers.
11) On pad printing graphic (One of the D Stands) - we custom design pad printing machinery 1-5 color with pneumatic and servo controls available. We offer, pads, cliches, rings, ink and other operating supplies. Same day shipping.
12) All designs should be vector files in AI or PDF format - 95 dpi is required.
13) If vector file logos are required we can supply for final booth design. Logos uploaded can be used as temporary logos.
14) www.qrbeamusa-example.com website should be somewhere on the booth - under the QRDyne logo?
15) A QR code pointing to our site (www.veltrane-example.com) should be on the booth, as well.
16) We May select your design but want to incorporate/add/amend/append final design depending on our team’s feedback.
17) Am example of the booth layout is attached but this should not be referenced for inspiration. We do not need our booth to look like this. It is just for general layout guidelines. THE “E” SECTION OF THE BOOTH WILL NOT STICK OUT LIKE THE ONE IN THE PHOTO. It is all one plane against the wall of the booth.

Thank you for taking the time to look at this.

Target Market(s)

Industrial Automation - Medical, Automotive, Packaging, Metal Processing

Industry/Entity Type

Industrial

Colors

Designer to choose colors to be used in the design.

Requirements
Must have
• A clean crisp feel. We are a fan of Plume’s use of simple straightforward marketing showing our product and what it can do.
• We cannot change the QR Dyne logo. This logo must be present on the tradeshow booth
Nice to have
• Please see the above notes in project description.
Should not have
• A dark theme. We like to keep things open and positive, so the tones of the booth should align with that.

```html
<!DOCTYPE html>
<html lang="en">
<head>
<meta charset="utf-8">
<title>Veltrane Engraving Systems – Laser Booth Back Wall</title>
<link rel="stylesheet" href="https://fonts.googleapis.com/css2?family=Bebas+Neue&family=Oswald:wght@600&family=Roboto:wght@400&display=swap">
<style>
  :root{
    --page:#ffffff;
    --wall-light:#f4f7f9;
    --wall-mid:#e3eaef;
    --wall-deep:#c8d6df;
    --prism:#dbe5ec;
    --steel-blue:#1f5f8b;
    --steel-blue-deep:#163f5e;
    --band-light:#ffffff;
    --text-slate:#1d3446;
    --rule-slate:#5b7486;
    --ink:#111111;
    --safety-red:#e3262b;
    --trim-blue:#2a4fa3;
  }
  html,body{margin:0;padding:0;width:1200px;height:707px;overflow:hidden;background:var(--page);}
  .template{display:block;width:1200px;height:707px;}
  .headline{font-family:"Bebas Neue",sans-serif;fill:var(--text-slate);font-size:24.5px;}
  .body-copy{font-family:"Oswald",sans-serif;font-weight:600;fill:var(--text-slate);font-size:9.4px;}
  .brand-name{font-family:"Bebas Neue",sans-serif;fill:var(--steel-blue-deep);}
  .partner-name{font-family:"Bebas Neue",sans-serif;fill:#ffffff;font-size:22px;}
  .partner-url{font-family:"Oswald",sans-serif;font-weight:600;fill:#ffffff;font-size:6.6px;}
  .qr-caption{font-family:"Oswald",sans-serif;font-weight:600;fill:var(--text-slate);font-size:6.6px;}
  .dimension{font-family:"Roboto",Arial,sans-serif;fill:var(--ink);font-size:16px;}
  .notice-title{font-family:"Roboto",Arial,sans-serif;fill:var(--safety-red);font-size:14.5px;}
  .notice-text{font-family:"Roboto",Arial,sans-serif;fill:var(--ink);font-size:11.8px;}
  .notice-head{font-family:"Roboto",Arial,sans-serif;fill:var(--ink);font-size:15px;}
</style>
</head>
<body>
<svg class="template" viewBox="0 0 1200 707" xmlns="http://www.w3.org/2000/svg">
  <defs>
    <linearGradient id="wall-fill" x1="0" y1="0" x2="1" y2="0.3">
      <stop offset="0" stop-color="var(--wall-light)"/>
      <stop offset="0.55" stop-color="var(--wall-mid)"/>
      <stop offset="1" stop-color="var(--wall-deep)"/>
    </linearGradient>
    <linearGradient id="prism-fill" x1="0" y1="0" x2="1" y2="1">
      <stop offset="0" stop-color="#ffffff"/>
      <stop offset="0.6" stop-color="var(--prism)"/>
      <stop offset="1" stop-color="#cfdce5"/>
    </linearGradient>
    <linearGradient id="streak-fill" x1="0" y1="0" x2="1" y2="1">
      <stop offset="0" stop-color="#1f5f8b" stop-opacity="0"/>
      <stop offset="0.45" stop-color="#1f5f8b" stop-opacity="0.7"/>
      <stop offset="0.75" stop-color="#1f5f8b" stop-opacity="0.55"/>
      <stop offset="1" stop-color="#1f5f8b" stop-opacity="0"/>
    </linearGradient>
    <linearGradient id="band-fill" x1="0" y1="0" x2="1" y2="0">
      <stop offset="0" stop-color="#ffffff"/>
      <stop offset="0.5" stop-color="var(--band-light)"/>
      <stop offset="1" stop-color="#f1f4f6"/>
    </linearGradient>
    <linearGradient id="partner-fill" x1="0" y1="0" x2="1" y2="0">
      <stop offset="0" stop-color="var(--steel-blue)"/>
      <stop offset="1" stop-color="var(--steel-blue-deep)"/>
    </linearGradient>
    <radialGradient id="circuit-fill">
      <stop offset="0" stop-color="#8fb0c6" stop-opacity="0.6"/>
      <stop offset="1" stop-color="#8fb0c6" stop-opacity="0"/>
    </radialGradient>
    <clipPath id="wall-clip">
      <path d="M23 57 Q23 28 52 28 L750 28 Q779 28 779 57 L779 634 L23 634 Z"/>
    </clipPath>
  </defs>

  <path class="bleed-frame" d="M16 55 Q16 21 50 21 L752 21 Q786 21 786 55 L786 641 L16 641 Z" fill="none" stroke="#222" stroke-width="0.7"/>

  <g class="wall-artwork" clip-path="url(#wall-clip)">
    <rect x="23" y="28" width="756" height="606" fill="url(#wall-fill)"/>
    <polygon class="prism" points="463,86 779,360 779,634 115,634" fill="url(#prism-fill)" opacity="0.8"/>
    <polygon class="light-streak" points="463,86 470,89 779,356 779,372" fill="url(#streak-fill)"/>
    <path class="brand-band" d="M432 244 L594 244 L678 149 L779 149 L779 224 L678 224 L594 290 L515 290 A121 121 0 0 0 432 244 Z" fill="url(#band-fill)"/>
    <path class="partner-band" d="M678 149 L779 149 L779 224 L678 224 Z" fill="url(#partner-fill)"/>
    <circle class="circuit-motif" role="img" aria-label="Circuit board pattern in dotted ring" cx="418" cy="362" r="100" fill="url(#circuit-fill)"/>
    <path class="ring" d="M418 242 A121 121 0 0 1 528 315" fill="none" stroke="var(--rule-slate)" stroke-width="1"/>
    <path class="ring" d="M503 449 A121 121 0 0 1 332 277" fill="none" stroke="var(--rule-slate)" stroke-width="1"/>

    <g class="brand-mark">
      <text class="brand-name" x="548" y="269" font-size="15" text-anchor="middle">VELTRANE</text>
      <text class="brand-name" x="548" y="277" font-size="7" text-anchor="middle">ENGRAVING SYSTEMS</text>
    </g>

    <g class="partner-mark">
      <text class="partner-name" x="690" y="190">QR DYNE</text>
      <text class="partner-url" x="690" y="205">WWW.QRBEAMUSA-EXAMPLE.COM</text>
    </g>

    <g class="message-left">
      <polyline points="124,128 124,373 297,373" fill="none" stroke="var(--rule-slate)" stroke-width="1"/>
      <text class="headline" x="140" y="152">LASER MARKING,</text>
      <text class="headline" x="140" y="178">WELDING, CLEANING</text>
      <text class="headline" x="140" y="204">AND CUTTING</text>
      <text class="body-copy" x="140" y="217">12 KW OF LASER POWER CUTS THROUGH 40 MM</text>
      <text class="body-copy" x="140" y="230">OF STAINLESS STEEL. FIBER, UV, CO2 AND</text>
      <text class="body-copy" x="140" y="243">GREEN SOURCES. PICO AND FEMTO PULSED.</text>
    </g>

    <g class="message-right">
      <line x1="593" y1="288" x2="593" y2="437" stroke="var(--rule-slate)" stroke-width="1"/>
      <text class="headline" x="607" y="302">CUSTOM</text>
      <text class="headline" x="607" y="328">BUILT</text>
      <text class="headline" x="607" y="354">SYSTEMS,</text>
      <text class="headline" x="607" y="380">ROBOTICS</text>
      <text class="headline" x="607" y="406">READY FOR</text>
      <text class="headline" x="607" y="432">YOUR LINE</text>
      <text class="body-copy" x="607" y="445">MARK GRAPHICS, WORDS,</text>
      <text class="body-copy" x="607" y="458">BAR CODES, QR CODES</text>
      <text class="body-copy" x="607" y="471">ON STATIONARY OR</text>
      <text class="body-copy" x="607" y="484">MOVING PARTS. CUT AND</text>
      <text class="body-copy" x="607" y="497">BORE CIRCUIT BOARDS.</text>
    </g>

    <g class="qr-slot">
      <rect x="700" y="535" width="58" height="58" rx="3" fill="#ffffff" stroke="var(--steel-blue-deep)" stroke-width="1.2" role="img" aria-label="QR code linking to www.veltrane-example.com"/>
      <text class="qr-caption" x="729" y="606" text-anchor="middle">WWW.VELTRANE-EXAMPLE.COM</text>
    </g>
  </g>

  <path class="safety-line" d="M31 60 Q31 36 55 36 L747 36 Q771 36 771 60 L771 625 L31 625 Z" fill="none" stroke="var(--safety-red)" stroke-width="0.6"/>

  <g class="dimension-height" stroke="#111" stroke-width="0.8">
    <line x1="794" y1="28" x2="828" y2="28"/>
    <line x1="794" y1="634" x2="828" y2="634"/>
    <line x1="811" y1="30" x2="811" y2="632"/>
    <polygon points="811,28 808,37 814,37" fill="#111" stroke="none"/>
    <polygon points="811,634 808,625 814,625" fill="#111" stroke="none"/>
  </g>
  <text class="dimension" x="829" y="313">2400mm</text>
  <text class="dimension" x="829" y="335">96″</text>

  <g class="dimension-width" stroke="#111" stroke-width="0.8">
    <line x1="23" y1="647" x2="23" y2="680"/>
    <line x1="779" y1="647" x2="779" y2="680"/>
    <line x1="25" y1="663" x2="777" y2="663"/>
    <polygon points="23,663 32,660 32,666" fill="#111" stroke="none"/>
    <polygon points="779,663 770,660 770,666" fill="#111" stroke="none"/>
  </g>
  <text class="dimension" x="341" y="679">3000mm</text>
  <text class="dimension" x="341" y="700">120″</text>

  <g class="notice-panel">
    <rect x="869.5" y="347.5" width="307" height="330" fill="#fff" stroke="#111" stroke-width="0.8"/>
    <text class="notice-title" x="874" y="377">Notice</text>
    <text class="notice-title" x="874" y="396">1″=25mm</text>
    <text class="notice-title" x="874" y="415">1′=300mm</text>
    <text class="notice-text" x="874" y="444">*The template  is in 100% acutual size.</text>
    <text class="notice-text" x="874" y="460">*File colour mode must be CMYK.</text>
    <text class="notice-text" x="874" y="476">*All text must be outlined</text>
    <text class="notice-text" x="881" y="491">(Type Menu -&gt; Create Outlines).</text>
    <text class="notice-text" x="874" y="507">*If Pantone colour matching is required</text>
    <text class="notice-text" x="881" y="523">specify the colours in the artwork.</text>
    <text class="notice-head" x="874" y="553">*Bleed Line</text>
    <line x1="874" y1="556.5" x2="972" y2="556.5" stroke="#111" stroke-width="1.5"/>
    <text class="notice-text" x="875" y="569">Art elements must extend to this line to account for</text>
    <text class="notice-text" x="875" y="585">slight inaccuracies when trimming</text>
    <text class="notice-head" x="874" y="606">*Trim Line</text>
    <line x1="874" y1="609" x2="972" y2="609" stroke="var(--trim-blue)" stroke-width="1.5"/>
    <text class="notice-text" x="875" y="620">Any text/logo/images past line wil be trimmed off</text>
    <text class="notice-head" x="874" y="645">*Safety Line</text>
    <line x1="874" y1="648.5" x2="972" y2="648.5" stroke="var(--safety-red)" stroke-width="1.5"/>
    <text class="notice-text" x="875" y="661">Important text/logos should not extend past this line</text>
  </g>
</svg>
</body>
</html>
```